Fish guide business card

Buisiness card

Target Market(s)

Visitors to Alder Cove BC wanting to catch fish in the ocean and have a memorable adventure fun filled day

Industry/Entity Type

Tourism

Contact Information for Business Card

Phone number 250 318 two cards Ray 250 318 6072 other card Lou 250 7396124 both have email info@rlmaplestoneoutings.com and website www.rlmaplestoneoutings.com

Requirements
Must have
• Email, website , name , phone , logo , Alder Cove BC
Nice to have
• Uploaded pictures have boat and man with fish picture

```html
<!DOCTYPE html>
<html lang="en">
<head>
<meta charset="UTF-8">
<title>RL Maplestone Outings — Business Card</title>
<link href="https://fonts.googleapis.com/css2?family=Poppins:wght@400;600&display=swap" rel="stylesheet">
<style>
  :root {
    --page: #e9e8e6;
    --card: #1b1b1b;
    --navy: #2b2570;
    --white: #ffffff;
    --shadow: rgba(0,0,0,0.28);
  }
  * { margin: 0; padding: 0; box-sizing: border-box; }
  html, body { width: 1200px; height: 842px; overflow: hidden; }
  body {
    background: var(--page);
    font-family: "Poppins", sans-serif;
    display: flex;
    flex-direction: column;
    align-items: center;
    justify-content: center;
    gap: 48px;
  }
  .card {
    position: relative;
    width: 620px;
    height: 354px;
    background: var(--card);
    box-shadow: 0 10px 28px var(--shadow);
    overflow: hidden;
  }

  /* Front */
  .side-tab {
    position: absolute;
    width: 44px;
    height: 56px;
    background: var(--navy);
  }
  .side-tab::after {
    content: "";
    position: absolute;
    top: 0;
    width: 4px;
    height: 100%;
    background: var(--white);
  }
  .side-tab--left { left: 0; top: 214px; }
  .side-tab--left::after { right: 0; }
  .side-tab--right { right: 0; top: 86px; }
  .side-tab--right::after { left: 0; }

  .brand {
    position: absolute;
    left: 50%;
    top: 50%;
    transform: translate(-42%, -56%);
    display: flex;
    align-items: center;
    gap: 16px;
  }
  .brand__dot {
    width: 26px;
    height: 26px;
    border-radius: 50%;
    background: var(--white);
    flex: none;
  }
  .brand__name {
    color: var(--white);
    font-weight: 600;
    font-size: 26px;
    letter-spacing: 1px;
    line-height: 1.2;
  }

  /* Back */
  .band {
    position: absolute;
    left: 0;
    width: 100%;
    height: 22px;
    background: var(--navy);
  }
  .band--top { top: 0; }
  .band--bottom { bottom: 0; }

  .contact {
    position: absolute;
    inset: 22px 0;
    display: flex;
    flex-direction: column;
    align-items: center;
    justify-content: center;
    color: var(--white);
    text-align: center;
    font-weight: 400;
    font-size: 17px;
    line-height: 1.35;
  }
  .contact__name {
    font-weight: 600;
    font-size: 22px;
    letter-spacing: 1px;
    text-transform: uppercase;
  }
  .contact__rule {
    width: 64px;
    height: 1.5px;
    background: var(--white);
    margin: 10px 0 12px;
  }
  .contact__place { font-size: 18px; margin-top: 6px; }
</style>
</head>
<body>
  <section class="card card--front">
    <div class="side-tab side-tab--left"></div>
    <div class="side-tab side-tab--right"></div>
    <div class="brand">
      <span class="brand__dot"></span>
      <span class="brand__name">RL Maplestone<br>Outings</span>
    </div>
  </section>

  <section class="card card--back">
    <div class="band band--top"></div>
    <div class="contact">
      <p class="contact__name">Ray</p>
      <span class="contact__rule"></span>
      <p class="contact__phone">250 318 6072</p>
      <p class="contact__email">info@rlmaplestoneoutings.com</p>
      <p class="contact__web">www.rlmaplestoneoutings.com</p>
      <span class="contact__rule"></span>
      <p class="contact__place">Alder Cove BC</p>
    </div>
    <div class="band band--bottom"></div>
  </section>
</body>
</html>
```